Business card design for Automotive workshop

We need a business card for a new automotive repair and tyre shop called Ridgeback Prime Automotive located in New Zealand. We are a clean, modern and fresh workshop and company.

Front needs to feature logo,
my name:
Lachie Westergaard (director)

Address:
48 Marlow Lane
Whitianga 3510

Phone: 07 842 1937
Mobile: 027 519 2764
Email: office@ridgebackmotors.co.nz
Website: ridgebackmotors.co.nz

Back needs to feature an area to write down appointment details, date and time.

Also feature a list of jobs and work we do such as,
Vehicle Servicing
All Mechanical Repairs
Warrant of Fitness
Tyres & Wheel Alignments
Automotive Diagnostics
Automotive Parts & Supplies

```html
<!DOCTYPE html>
<html lang="en">
<head>
<meta charset="utf-8">
<title>Ridgeback Prime Automotive – Business Card</title>
<link rel="stylesheet" href="https://fonts.googleapis.com/css2?family=Roboto:wght@400;500;700;900&display=swap">
<style>
  :root {
    --backdrop: #a58a66;
    --card: #f7f7f7;
    --red: #e3202a;
    --red-dark: #b3141c;
    --ink: #2b2b2b;
    --ink-soft: #444444;
    --white: #ffffff;
  }
  * { margin: 0; padding: 0; box-sizing: border-box; }
  html, body {
    width: 900px; height: 1200px; overflow: hidden;
    background: var(--backdrop);
    font-family: "Roboto", Arial, sans-serif;
    color: var(--ink);
  }
  .canvas { position: relative; width: 900px; height: 1200px; }

  .card {
    position: absolute; left: 72px; width: 756px; height: 432px;
    background: var(--card); border-radius: 20px; overflow: hidden;
    box-shadow: 0 10px 24px rgba(0,0,0,0.28);
  }
  .card--front { top: 140px; }
  .card--back { top: 630px; }

  .card__band {
    position: absolute; left: 0; right: 0; bottom: 0; height: 78px;
    background: var(--red); border-bottom: 8px solid var(--red-dark);
    color: var(--white); font-size: 24px; font-weight: 500;
    display: flex; align-items: center; justify-content: center;
  }

  /* Front */
  .brand {
    position: absolute; top: 48px; left: 0; right: 0; text-align: center;
  }
  .brand__name {
    font-size: 46px; font-weight: 900; color: var(--red);
    letter-spacing: 1px; text-transform: uppercase; line-height: 1;
  }
  .brand__rule {
    margin: 14px auto 0; width: 560px; height: 3px; background: var(--ink);
  }
  .person { position: absolute; top: 176px; left: 0; right: 0; text-align: center; }
  .person__name { font-size: 32px; font-weight: 700; color: var(--red); text-transform: uppercase; letter-spacing: 1px; }
  .person__role { margin-top: 6px; font-size: 20px; font-weight: 700; color: var(--ink); letter-spacing: 1px; }

  .contacts {
    position: absolute; top: 270px; left: 120px; right: 60px;
    display: grid; grid-template-columns: 230px 1fr; row-gap: 14px; column-gap: 40px;
  }
  .contact { display: flex; align-items: center; gap: 14px; font-size: 21px; font-weight: 500; color: var(--ink-soft); }
  .contact svg { width: 24px; height: 24px; flex: none; }

  /* Back */
  .heading {
    position: absolute; top: 56px; left: 0; right: 0;
    display: flex; align-items: center; justify-content: center; gap: 20px;
  }
  .heading__title { font-size: 44px; font-weight: 500; color: var(--red); letter-spacing: 6px; }
  .heading__lines { width: 70px; height: 12px; }

  .fields {
    position: absolute; top: 160px; left: 60px; right: 60px;
    display: flex; justify-content: space-between;
  }
  .field { display: flex; align-items: flex-end; gap: 14px; font-size: 30px; font-weight: 700; letter-spacing: 3px; }
  .field__line { width: 190px; border-bottom: 2px solid var(--ink); margin-bottom: 6px; }

  .services {
    position: absolute; top: 246px; left: 60px; right: 40px;
    display: grid; grid-template-columns: 340px 1fr; row-gap: 14px; list-style: none;
  }
  .service { display: flex; align-items: center; gap: 12px; font-size: 21px; font-weight: 500; color: var(--ink-soft); }
  .service svg { width: 24px; height: 24px; flex: none; }
</style>
</head>
<body>
<main class="canvas">

  <section class="card card--front" aria-label="Business card front">
    <header class="brand">
      <div class="brand__name">Ridgeback Prime Automotive</div>
      <div class="brand__rule"></div>
    </header>

    <div class="person">
      <div class="person__name">Lachie Westergaard</div>
      <div class="person__role">DIRECTOR</div>
    </div>

    <div class="contacts">
      <div class="contact">
        <svg viewBox="0 0 24 24" aria-hidden="true"><path fill="var(--red)" d="M4 9c0-3 3-5 8-5s8 2 8 5l-4 1-1-3H9L8 10 4 9zm3 3h10l2 8H5l2-8zm5 1.5a2.5 2.5 0 1 0 0 5 2.5 2.5 0 0 0 0-5z"/></svg>
        <span>07 842 1937</span>
      </div>
      <div class="contact">
        <svg viewBox="0 0 24 24" aria-hidden="true"><rect x="3" y="5" width="18" height="14" rx="2" fill="var(--red)"/><path d="M4 7l8 6 8-6" stroke="var(--white)" stroke-width="1.8" fill="none"/></svg>
        <span>office@ridgebackmotors.co.nz</span>
      </div>
      <div class="contact">
        <svg viewBox="0 0 24 24" aria-hidden="true"><rect x="6" y="2" width="12" height="20" rx="2.5" fill="var(--red)"/><rect x="8" y="5" width="8" height="12" fill="var(--white)"/><circle cx="12" cy="19.3" r="1" fill="var(--white)"/></svg>
        <span>027 519 2764</span>
      </div>
      <div class="contact">
        <svg viewBox="0 0 24 24" aria-hidden="true"><circle cx="12" cy="12" r="10" fill="var(--red)"/><g stroke="var(--white)" stroke-width="1.4" fill="none"><ellipse cx="12" cy="12" rx="4" ry="9"/><path d="M3 12h18M5 7h14M5 17h14"/></g></svg>
        <span>www.ridgebackmotors.co.nz</span>
      </div>
    </div>

    <footer class="card__band">48 Marlow Lane, Whitianga 3510</footer>
  </section>

  <section class="card card--back" aria-label="Business card back">
    <div class="heading">
      <svg class="heading__lines" viewBox="0 0 70 12" aria-hidden="true"><rect y="0" width="70" height="4" fill="var(--ink)"/><rect x="20" y="8" width="50" height="4" fill="var(--ink)"/></svg>
      <h2 class="heading__title">APPOINTMENT</h2>
      <svg class="heading__lines" viewBox="0 0 70 12" aria-hidden="true"><rect y="0" width="70" height="4" fill="var(--ink)"/><rect y="8" width="50" height="4" fill="var(--ink)"/></svg>
    </div>

    <div class="fields">
      <div class="field"><span>DATE</span><span class="field__line"></span></div>
      <div class="field"><span>TIME</span><span class="field__line"></span></div>
    </div>

    <ul class="services">
      <li class="service"><svg viewBox="0 0 24 24" aria-hidden="true"><circle cx="12" cy="12" r="11" fill="var(--red)"/><path d="M7 12.5l3.2 3.2L17 9" stroke="var(--white)" stroke-width="2.4" fill="none"/></svg>Vehicle Servicing</li>
      <li class="service"><svg viewBox="0 0 24 24" aria-hidden="true"><circle cx="12" cy="12" r="11" fill="var(--red)"/><path d="M7 12.5l3.2 3.2L17 9" stroke="var(--white)" stroke-width="2.4" fill="none"/></svg>Tyres &amp; Wheel Alignments</li>
      <li class="service"><svg viewBox="0 0 24 24" aria-hidden="true"><circle cx="12" cy="12" r="11" fill="var(--red)"/><path d="M7 12.5l3.2 3.2L17 9" stroke="var(--white)" stroke-width="2.4" fill="none"/></svg>All Mechanical Repairs</li>
      <li class="service"><svg viewBox="0 0 24 24" aria-hidden="true"><circle cx="12" cy="12" r="11" fill="var(--red)"/><path d="M7 12.5l3.2 3.2L17 9" stroke="var(--white)" stroke-width="2.4" fill="none"/></svg>Automotive Diagnostics</li>
      <li class="service"><svg viewBox="0 0 24 24" aria-hidden="true"><circle cx="12" cy="12" r="11" fill="var(--red)"/><path d="M7 12.5l3.2 3.2L17 9" stroke="var(--white)" stroke-width="2.4" fill="none"/></svg>Warrant of Fitness</li>
      <li class="service"><svg viewBox="0 0 24 24" aria-hidden="true"><circle cx="12" cy="12" r="11" fill="var(--red)"/><path d="M7 12.5l3.2 3.2L17 9" stroke="var(--white)" stroke-width="2.4" fill="none"/></svg>Automotive Parts &amp; Supplies</li>
    </ul>

    <footer class="card__band">www.ridgebackmotors.co.nz</footer>
  </section>

</main>
</body>
</html>
```